Very basic draft completed. Need someone to apply their creative magic

I am building a new website for my business and looking for a designer to assist me on a part-time basis.

My business is a booking site for classes and lessons. It is essentially a directory service, and needs to conform to a standard web-layout that is easy to navigate and familiar to users (i.e. nothing to creative). The function and structure i have adopted is common amongst sites like quolt, hotel booking services, etc.

The first task on my list is to develop the main page. I have already compiled a draft of the first page using Fireworks (see attached) and am looking for someone to cast their creative magic to this draft while maintaining the general layout of the page. After the main page is developed, I will be looking for the same designer to assist with the rest of the site.

Design wise, I'd like to go for a slightly retro feel
By this I mean a moderately modern page with a spark of retro here and there. If you look at my draft you'll notice that I've used regular font for most text, and retro/old-school fonts for surburb names.

I happy for you to suggest colours, but regular page elements such as web links need to remain standard (i.e links = blue) so that they are familiar and identifiable to my users.

Other points:
1) I don't want the page to be too dark (dark headings, images and borders are fine, but I'd like to maintain white or light backgrounds)

2) Positioning: The Body should be centred, with the Header and Footer extending across the hole screen (as illustrated in my draft)

3) I'm happy if the design includes images from photostock libraries.The Silhoute picture for my draft were choosen because there are hundreds of them, and I can regularly change them on the site - keeping it fresh and new. I'd be very happy if the design incorporate images that could also be place often using photo stock images (i.e. happy to keep silhoutes, but leave it to you to decide what looks best)

Note: I'm happy for you to "copy" art work from any photo stock site, and I will pay for the full quality images when the design is selected.

4) The page Footer needs a lot of attention. It will contain standard Footer links/elements.

5) You are free to do anything to the Header section. It needs to have login/register elements

I'm happy to provide further comments, or review other sites/work to help direct design work.

Hi All,

I've updated the project brief, eliminating many of the requirements and giving you the freedom with design submissions, etc. I've also added the $20 payment for submissions. 
Cheers,
Morwen

Reason: I'm away on holiday and will review your submissions and provide feedback when I get back.

```html
<!DOCTYPE html>
<html lang="en">
<head>
<meta charset="utf-8">
<title>Step Outside – Explore Courses &amp; Activities</title>
<link rel="stylesheet" href="https://fonts.googleapis.com/css2?family=Arimo:wght@400;700&display=swap">
<style>
:root{
  --pink:#e2367c;
  --magenta:#b8306e;
  --orchid:#d69bd0;
  --orchid-dark:#b7599f;
  --orchid-light:#ecc9e8;
  --lavender:#f6e6f4;
  --ink:#2b2b2b;
  --grey:#777;
  --title:#b0155e;
  --line:#d58fcf;
  --white:#fff;
}
*{box-sizing:border-box;margin:0;padding:0}
html,body{width:1084px;height:1200px;overflow:hidden}
body{position:relative;background:var(--white);font-family:"Arimo",Arial,sans-serif;color:var(--ink)}
.abs{position:absolute}

/* header */
.brand{left:57px;top:28px;display:flex;align-items:center;gap:10px}
.brand-mark{width:56px;height:44px;background:var(--magenta);border-radius:6px}
.brand-name{font-size:34px;font-weight:700;color:#3a3a3a;letter-spacing:-.5px}
.tagline{left:137px;top:67px;font-size:11px;letter-spacing:.5px;color:#444}
.search{left:659px;top:51px;width:172px;height:22px;border:1px solid var(--orchid);background:var(--lavender);color:#c98bc4;font-size:12px;padding:4px 6px}
.search-btn{left:837px;top:51px;width:30px;height:22px;background:var(--magenta)}
.login{left:903px;top:46px;width:100px;height:30px;background:var(--orchid);border:2px solid #e7c3e3;font-size:17px;text-align:center;line-height:26px;color:#333}

/* page */
.page{left:52px;top:110px;width:968px;height:1072px;background:var(--white);box-shadow:0 0 5px rgba(0,0,0,.35)}

/* explore menu */
.explore-bg{left:69px;top:126px;width:249px;height:326px;background:var(--orchid-light);border:1px solid var(--orchid)}
.explore-title{left:69px;top:126px;width:249px;height:34px;background:var(--pink);color:var(--white);font-size:17px;padding:9px 11px}
.menu{left:71px;top:166px;width:240px;list-style:none}
.menu li{height:31.6px;background:var(--orchid);border-bottom:2px solid var(--orchid-light);font-size:13px;padding:8px 25px;position:relative}
.menu li::after{content:"»";position:absolute;right:34px;top:3px;font-size:20px;color:#efd3ec}
.menu li.active{background:var(--orchid-dark);color:var(--white)}
.menu li.active::after{content:none}
.submenu{left:313px;top:301px;width:165px;list-style:none;z-index:2}
.submenu li{height:31.5px;background:rgba(176,72,150,.88);border-bottom:2px solid rgba(240,190,230,.6);color:var(--white);font-size:13px;padding:8px 17px}
.hero{left:318px;top:126px;width:686px;height:326px;border:1px solid #aaa;background:radial-gradient(circle at 60% 40%,#fbe6f3 0%,#f2a6d3 35%,#dc3f96 70%,#a2286e 100%)}

/* search bar */
.label{font-size:13px}
.filter-bar{left:69px;top:493px;width:933px;height:81px;border:2px solid var(--white);box-shadow:0 0 4px rgba(0,0,0,.35);display:flex}
.filter-bar > div{height:100%;position:relative}
.f-range{width:199px;background:var(--white);font-size:10px}
.f-date{width:162px;background:var(--orchid);border-left:2px solid var(--white)}
.f-days{width:289px;background:var(--orchid);border-left:2px solid var(--white)}
.f-loc{width:184px;background:var(--orchid);border-left:2px solid var(--white)}
.f-go{flex:1;background:var(--orchid);border-left:2px solid var(--white)}
.slider{position:absolute;left:36px;width:122px;height:10px;border:2px solid #ccc;background:var(--white)}
.slider i{position:absolute;top:0;left:5px;right:5px;height:3px;top:2px;background:#888}
.slider b{position:absolute;top:-3px;width:12px;height:12px;border-radius:50%;background:#3a7bd5;border:2px solid #bcd}
.datebox{position:absolute;left:60px;width:85px;height:20px;background:var(--white);font-size:11px;text-align:center;line-height:20px}
.day{position:absolute;font-size:12px;display:flex;align-items:center;gap:10px}
.day span{width:12px;height:12px;border:1px solid #888;background:var(--white);border-radius:2px}
.select{position:absolute;left:16px;top:28px;width:150px;height:20px;background:var(--white);border:1px solid #bbb}
.select b{position:absolute;right:1px;top:1px;width:16px;height:16px;background:var(--orchid-dark);border:1px solid #888}
.filter-btn{position:absolute;left:16px;top:22px;width:80px;height:32px;background:var(--white);font-size:17px;text-align:center;line-height:32px}

/* courses */
.bar{height:26px;background:var(--orchid);font-size:13px;padding:6px 14px}
.courses-bar{left:69px;top:593px;width:574px}
.pager{left:609px;top:598px}
.card{width:170px}
.card-img{width:162px;height:137px;border:4px solid #c8c8c8}
.card-img.a{background:linear-gradient(135deg,#f4f4f4,#e3b8b8 55%,#c72a2a)}
.card-img.b{background:linear-gradient(160deg,#5a2a20,#20100c 60%,#b8b06a)}
.card-img.c{background:linear-gradient(150deg,#4d4038,#8a6f60 55%,#c78aa8)}
.card-title{margin-top:6px;font-size:13px;font-weight:700;color:var(--title);letter-spacing:.5px;line-height:16px}
.card-sub{font-size:10.5px;font-style:italic;color:var(--grey);line-height:15px;margin-top:1px;min-height:30px}
.card-text{font-size:10.5px;line-height:14px;margin-top:6px}
.card-text a{color:#cf8fc9;text-decoration:none;margin-left:6px}

/* location */
.loc-bar{left:658px;top:593px;width:344px}
.loc-select{position:absolute;left:17px;top:4px;width:130px;height:18px;background:var(--white);border:1px solid #999;font-size:12px;color:#555;padding:1px 5px}
.loc-box{left:658px;top:623px;width:344px;height:232px;border:1px solid var(--line)}
.map-icon{left:670px;top:632px;width:36px;height:36px;border-radius:7px;background:linear-gradient(#fdf9e8,#e8dcae);border:1px solid #ccc}
.place{left:722px;top:640px;font-size:16px}
.tab{left:659px;width:125px;height:22px;background:var(--orchid);font-size:13px;padding:4px 12px}
.rule{left:784px;width:216px;height:1px;background:var(--line)}
.sched{left:680px;top:710px;font-size:12px;display:grid;grid-template-columns:50px 49px 49px 44px 43px 43px 30px;row-gap:8px}
.sched b{font-weight:700}

/* footer */
.footer{left:69px;top:879px;width:935px;height:240px;border-top:4px solid var(--orchid);background:linear-gradient(#f0cfec,#fbf1f9 55%,var(--white))}
.foot-col{position:absolute;top:30px;list-style:none;font-size:13px;color:#444;line-height:23.6px}
.foot-rule{left:69px;top:1126px;width:935px;height:1px;background:var(--orchid)}
.copy{left:0;width:1060px;top:1147px;text-align:center;font-size:9.5px;color:#555}
</style>
</head>
<body>

<header>
  <div class="abs brand"><span class="brand-mark"></span><span class="brand-name">Step Outside</span></div>
  <div class="abs tagline">GET OUT AND DISCOVER SOMETHING NEW</div>
  <div class="abs search">Search courses by keyword</div>
  <div class="abs search-btn">
    <svg width="30" height="22" viewBox="0 0 30 22"><circle cx="14" cy="10" r="4" fill="none" stroke="#fff" stroke-width="2"/><line x1="17" y1="13" x2="21" y2="17" stroke="#fff" stroke-width="2.5"/></svg>
  </div>
  <div class="abs login">Login</div>
</header>

<main>
  <div class="abs page"></div>

  <div class="abs explore-bg"></div>
  <div class="abs explore-title">Explore Courses &amp; Acitvities</div>
  <ul class="abs menu">
    <li>Visual arts</li><li>Cooking</li><li>Health / Fitness</li><li>Home / Life</li>
    <li class="active">Languages</li><li>Performing arts</li><li>Professional</li><li>Tech / Internet</li><li>Arts and Science</li>
  </ul>
  <div class="abs hero" role="img" aria-label="Photo of two women dancing joyfully against a pink light-swirl background"></div>
  <ul class="abs submenu"><li>Danish</li><li>French</li><li>German</li><li>Spanish</li></ul>

  <div class="abs label" style="left:73px;top:471px">Refine Search</div>
  <div class="abs label" style="left:280px;top:471px">Optional Search</div>

  <div class="abs filter-bar">
    <div class="f-range">
      <div class="abs" style="left:13px;top:5px">Age : 18 yrs +</div>
      <div class="slider" style="top:23px"><i></i><b style="left:68px"></b></div>
      <div class="abs" style="left:13px;top:43px">Max Price : $ 50</div>
      <div class="slider" style="top:60px"><i></i><b style="left:32px"></b></div>
    </div>
    <div class="f-date">
      <div class="abs" style="left:12px;top:34px;font-size:13px">Date :</div>
      <div class="datebox" style="top:12px">15 / 12 / 2011</div>
      <div class="abs" style="left:96px;top:34px;font-size:11px">to</div>
      <div class="datebox" style="top:49px">15 / 01 / 2012</div>
    </div>
    <div class="f-days">
      <div class="day" style="left:16px;top:18px"><span></span>Mon</div>
      <div class="day" style="left:84px;top:18px"><span></span>Wed</div>
      <div class="day" style="left:156px;top:18px"><span></span>Fri</div>
      <div class="day" style="left:220px;top:18px"><span></span>Sun</div>
      <div class="day" style="left:16px;top:52px"><span></span>Tue</div>
      <div class="day" style="left:84px;top:52px"><span></span>Thu</div>
      <div class="day" style="left:156px;top:52px"><span></span>Sat</div>
      <div class="day" style="left:220px;top:52px"><span></span>All</div>
    </div>
    <div class="f-loc"><div class="select"><b></b></div></div>
    <div class="f-go"><div class="filter-btn">Filter</div></div>
  </div>

  <div class="abs bar courses-bar">All Courses &amp; Activities</div>
  <svg class="abs pager" width="22" height="16" viewBox="0 0 22 16"><path d="M8 2 2 8l6 6M14 2l6 6-6 6" fill="none" stroke="#fff" stroke-width="3"/></svg>

  <article class="abs card" style="left:71px;top:637px">
    <div class="card-img a" role="img" aria-label="Photo of a salsa dancing couple in red and black"></div>
    <div class="card-title">Salsa Patterns</div>
    <div class="card-sub">with Rio Sol salsa dance company</div>
    <div class="card-text">Lorem Ipsum is simply dumy text of the printing <a href="#">More &gt;&gt;</a></div>
  </article>
  <article class="abs card" style="left:272px;top:637px">
    <div class="card-img b" role="img" aria-label="Photo of ballroom dancers performing on stage"></div>
    <div class="card-title">Ballroom Dancing for Bigners</div>
    <div class="card-sub" style="min-height:15px">with Stride dance studios</div>
    <div class="card-text">Lorem Ipsum is simply dumy text of the printing <a href="#">More &gt;&gt;</a></div>
  </article>
  <article class="abs card" style="left:479px;top:637px">
    <div class="card-img c" role="img" aria-label="Photo of a couple dancing the tango"></div>
    <div class="card-title">Argentine Tango</div>
    <div class="card-sub">with Stride dance studios</div>
    <div class="card-text">Lorem Ipsum is simply dumy text of the printing <a href="#">More &gt;&gt;</a></div>
  </article>

  <div class="abs bar loc-bar"><div class="loc-select">Select Location&nbsp;&nbsp;&nbsp;&nbsp;▾</div></div>
  <div class="abs loc-box"></div>
  <div class="abs map-icon"></div>
  <svg class="abs" style="left:676px;top:640px" width="24" height="24" viewBox="0 0 24 24"><path d="M12 2a6 6 0 0 0-6 6c0 5 6 12 6 12s6-7 6-12a6 6 0 0 0-6-6z" fill="#e23b3b"/><circle cx="12" cy="8" r="2.2" fill="#fff"/></svg>
  <div class="abs place">Riverbend</div>
  <div class="abs tab" style="top:678px">Schedule</div>
  <div class="abs rule" style="top:699px"></div>
  <div class="abs sched">
    <b>Mon</b><b>Tue</b><b>Wed</b><b>Thu</b><b>Fri</b><b>Sat</b><b>Sun</b>
    <span>6 pm</span><span>6 pm,<br>7pm</span><span>6 pm</span><span></span><span></span><span></span><span></span>
  </div>
  <div class="abs tab" style="top:780px">Price</div>
  <div class="abs rule" style="top:801px"></div>
  <div class="abs" style="left:679px;top:820px;font-size:16px">$ 15</div>
  <div class="abs" style="left:740px;top:812px;font-size:12px;line-height:18px">Single<br>Session</div>
</main>

<footer>
  <div class="abs footer">
    <ul class="foot-col" style="left:26px"><li>Visual arts</li><li>Cooking</li><li>Health / Fitness</li><li>Home / Life</li><li>Languages</li><li>Performing arts</li></ul>
    <ul class="foot-col" style="left:207px"><li>Visual arts</li><li>Cooking</li><li>Health / Fitness</li><li>Home / Life</li><li>Languages</li><li>Performing arts</li><li>Professional</li></ul>
    <ul class="foot-col" style="left:405px"><li>Visual arts</li><li>Cooking</li><li>Health / Fitness</li><li>Home / Life</li><li>Languages</li><li>Performing arts</li><li>Professional</li><li>Tech / Internet</li><li>Arts and Science</li></ul>
    <ul class="foot-col" style="left:599px"><li>Visual arts</li><li>Cooking</li><li>Health / Fitness</li><li>Home / Life</li><li>Languages</li><li>Performing arts</li><li>Professional</li></ul>
    <ul class="foot-col" style="left:784px"><li>Visual arts</li><li>Cooking</li><li>Health / Fitness</li><li>Home / Life</li><li>Languages</li><li>Performing arts</li></ul>
  </div>
  <div class="abs foot-rule"></div>
  <div class="abs copy">All Rights Reserved, Step Outside 2012</div>
</footer>

</body>
</html>
```